Business Card Design Project

We are a distribution company providing goods to Latin America. We sell everything from Medical equipment, generic medicines, to carecliners. The logo that we use is attached. The logo can incorporate different colors other than black for versatility. The company name is Valdoria International Corporation and/or VIC. The card will be printed using 1 or more of the following: Silk mounted and/or embossed. So if the design ideas could be made to incorporate that technique or any other unique techniques, it would be great. The target market is dialysis centers/doctors.

Basic Info for card:
Marnie Dowsett
Purchasing Manager
555-317-4086 direct
555-241-7953 fax
marnie.dowsett@valdoriavic.example
www.valdoriavic.example

Target Market(s)

Latin America

Industry/Entity Type

Business

Requirements
Nice to have
• The Front of the card should have the basic contact information with company name/logo. The back of the card could incorporate

```html
<!DOCTYPE html>
<html lang="en">
<head>
<meta charset="utf-8">
<title>Valdoria International Corporation — Business Card</title>
<link href="https://fonts.googleapis.com/css2?family=Arimo:wght@400;700&display=swap" rel="stylesheet">
<style>
  :root {
    --stage: #d9d6d2;
    --paper: #ffffff;
    --ink-grey: #7a7a7a;
    --ink-dark: #555555;
    --brand-red: #e8262c;
    --brand-red-deep: #c81d22;
    --brand-red-light: #ef3a3a;
    --ghost: #ececec;
  }
  * { box-sizing: border-box; margin: 0; padding: 0; }
  html, body {
    width: 1102px; height: 1200px; overflow: hidden;
    background: var(--stage);
    font-family: "Arimo", Arial, sans-serif;
  }
  .sheet {
    position: relative; width: 1102px; height: 1200px;
  }
  .card {
    position: absolute; left: 101px; width: 900px; height: 514px;
    box-shadow: 0 6px 24px rgba(0,0,0,.18);
    overflow: hidden;
  }
  .card--info { top: 57px; background: var(--paper); }
  .card--brand {
    top: 628px;
    background: linear-gradient(135deg, var(--brand-red-light) 0%, var(--brand-red) 45%, var(--brand-red-deep) 100%);
  }

  /* Info side */
  .company {
    position: absolute; left: 80px; top: 70px;
    font-size: 30px; line-height: 34px; color: var(--ink-grey);
  }
  .person {
    position: absolute; left: 80px; top: 170px;
  }
  .person::before {
    content: ""; position: absolute; left: -80px; top: 2px;
    width: 14px; height: 58px; background: var(--brand-red);
  }
  .person__name {
    font-size: 34px; color: var(--brand-red); line-height: 40px;
  }
  .person__title {
    font-size: 12px; letter-spacing: 2px; text-transform: uppercase;
    color: var(--brand-red); margin-top: 2px;
  }
  .address {
    position: absolute; left: 80px; top: 268px;
    font-size: 21px; line-height: 26px; color: var(--ink-dark);
    font-style: normal;
  }
  .contacts {
    position: absolute; left: 80px; top: 350px; list-style: none;
    font-size: 21px; line-height: 32px; color: var(--ink-dark);
  }
  .contacts__label { display: inline-block; width: 36px; }
  .ghost-mark {
    position: absolute; right: 50px; top: 90px;
    font-size: 200px; font-weight: 700; color: var(--ghost);
    letter-spacing: 4px;
  }

  /* Brand side */
  .brand-mark {
    position: absolute; left: 0; right: 0; top: 130px;
    display: flex; justify-content: center; align-items: center; gap: 26px;
  }
  .brand-mark__dot {
    width: 70px; height: 70px; border-radius: 50%; background: var(--paper);
  }
  .brand-mark__name {
    font-size: 120px; font-weight: 700; color: var(--paper); letter-spacing: 6px;
  }
  .website {
    position: absolute; left: 0; right: 0; top: 380px; text-align: center;
    font-size: 32px; letter-spacing: 3px; color: var(--paper);
  }
</style>
</head>
<body>
<main class="sheet">
  <section class="card card--info" aria-label="Card contact side">
    <p class="company">Valdoria International<br>Corporation</p>
    <div class="person">
      <p class="person__name">Marnie Dowsett</p>
      <p class="person__title">Purchasing Manager</p>
    </div>
    <address class="address">1480 NE 7th Avenue<br>Port Alder, FL 00135</address>
    <ul class="contacts">
      <li><span class="contacts__label">T:</span>(555)317-4086</li>
      <li><span class="contacts__label">F:</span>(555) 241-7953</li>
      <li><span class="contacts__label">E:</span>marnie.dowsett@valdoriavic.example</li>
    </ul>
    <span class="ghost-mark" aria-hidden="true">VIC</span>
  </section>

  <section class="card card--brand" aria-label="Card brand side">
    <div class="brand-mark">
      <span class="brand-mark__dot"></span>
      <span class="brand-mark__name">VIC</span>
    </div>
    <p class="website">www.valdoriavic.example</p>
  </section>
</main>
</body>
</html>
```